Vorsa -Letter Head

We are predominantly a residential home builder based in Melbourne, Victoria Australia. We construct houses, apartments, townhouses, multi-unit developments.

The name of the company is "Vorsa"
My company believes in building unique construction projects mainly residential homes. The target customers are upmarket Melbourne residents/investors.

I want the brand name "Vorsa" to be part of the logo. There's no need to put the word construction in the logo at this stage.

I would also like some ideas for a slogan. But I would like something unique and different for a slogan not the same old cliche.

Industry/Entity Type

Construction

Requirements
Must have
• I need to be able to print quotes, general letters for customers, print tables and pictures on the letter head. So it must not have too much graphics and should be simple.

```html
<!DOCTYPE html>
<html lang="en">
<head>
<meta charset="utf-8">
<title>Vorsa – Letterhead</title>
<link rel="stylesheet" href="https://fonts.googleapis.com/css2?family=Questrial&display=swap">
<style>
  :root {
    --backdrop: #ececec;
    --paper: #f4f4f4;
    --navy: #0b0d45;
    --cyan: #17b3dc;
    --stripe: #d3e7ec;
    --ink: #3a3a3a;
    --white: #ffffff;
  }
  * { margin: 0; padding: 0; box-sizing: border-box; }
  html, body {
    width: 1200px;
    height: 795px;
    overflow: hidden;
    background: var(--backdrop);
    font-family: "Questrial", "Century Gothic", sans-serif;
  }
  .letterhead {
    position: absolute;
    left: 340px;
    top: 30px;
    width: 520px;
    height: 735px;
    background: var(--paper);
    box-shadow: 0 2px 10px rgba(0,0,0,0.08);
    overflow: hidden;
  }
  .header-band {
    position: absolute;
    left: 0; top: 0;
    width: 100%;
    height: 76px;
    background: var(--navy);
  }
  .brand {
    position: absolute;
    left: 26px;
    bottom: 10px;
    display: flex;
    align-items: center;
    gap: 7px;
  }
  .brand-square {
    width: 12px;
    height: 12px;
    background: var(--cyan);
  }
  .brand-name {
    color: var(--cyan);
    font-size: 26px;
    letter-spacing: 0.5px;
    line-height: 1;
  }
  .decor-area {
    position: absolute;
    left: 300px;
    top: 340px;
    width: 220px;
    height: 373px;
    background: linear-gradient(180deg, rgba(211,231,236,0) 0%, var(--stripe) 45%, var(--stripe) 100%);
  }
  .contact {
    position: absolute;
    left: 26px;
    bottom: 42px;
    font-size: 10px;
    color: var(--ink);
    line-height: 1.75;
  }
  .contact-label {
    display: inline-block;
    width: 16px;
    font-weight: bold;
  }
  .footer-band {
    position: absolute;
    left: 0; bottom: 0;
    width: 100%;
    height: 22px;
    background: var(--cyan);
    display: flex;
    align-items: center;
    justify-content: flex-end;
    padding-right: 26px;
  }
  .address {
    color: var(--white);
    font-size: 9px;
    letter-spacing: 0.6px;
    text-transform: uppercase;
    white-space: nowrap;
  }
</style>
</head>
<body>
  <main class="letterhead">
    <header class="header-band">
      <div class="brand">
        <span class="brand-square"></span>
        <span class="brand-name">Vorsa</span>
      </div>
    </header>

    <div class="decor-area" role="img" aria-label="Faint light-blue decorative graphic in the lower right corner"></div>

    <div class="contact">
      <div><span class="contact-label">T</span>123 456 7890</div>
      <div><span class="contact-label">M</span>987 654 3210</div>
      <div><span class="contact-label">E</span>helpdesk@youremail.com</div>
    </div>

    <footer class="footer-band">
      <span class="address">Address Line 1, Address Line 2, City, Country, Zip - 654321</span>
    </footer>
  </main>
</body>
</html>
```